Redesign of Plastic Surgeon Website to fully responsive / modern feel

Hi

Our current website is out of date www.harbourlinecosmetic.org

We want a fresh / modern looking design
Needs to be fully responsive design that works extremely well on ipad and mobile device

Would like design for both full screen website and mobile

Have listed a few websites of other plastic surgeons we like
http://www.reformclinicdaily.com/
http://www.peterholtbymd.com/
http://www.corvanbeauty.com/
http://www.tidewellcontouring.com/

Menu needs to include
1. About Us
2. Procedures (see current website for example)
3. News
4. Patient Resources
5. Contact Us

We are flexible with colours / images / layout

I have uploaded a document that has some content - the face pages content is completed only

some of the procedures can have content upwards of 4000 words - total website can be large with over 40,000 words
Updates

Target Market(s)

Mainly women 20-60 85% of practice
Some men 15%

Industry/Entity Type

Plastic Surgery

Number of Pages Required

5+ page

Requirements
Must have
• We need designs for
• Homepage
• Internal pages
• 1. Landing pages for breast / body / face / non surgical main pages
• 2. Procedure pages for individual pages under each section - eg breast augmentation
• 3. About us pages - like meet the doctor, our staff, clinics
• 4. Contact page
• 5. Blog / News page
Nice to have
• See our list of websites for examples of designs we like
• Like full screen design with nice hero image
• Needs to have good to call to action messages on home page like
• Specials, procedure of the month, etc

```html
<!DOCTYPE html>
<html lang="en">
<head>
<meta charset="utf-8">
<title>Harbourline Cosmetic — Home</title>
<link rel="stylesheet" href="https://fonts.googleapis.com/css2?family=Raleway:wght@400;500;600;700&display=swap">
<style>
  :root{
    --red:#e8213f;
    --red-soft:#f0525f;
    --ink:#222329;
    --muted:#45464d;
    --hero-dark:#120207;
    --card-bg:rgba(22,6,10,.72);
    --card-title-muted:#9aa0b0;
    --white:#ffffff;
    --rule:#8a93a6;
  }
  *{box-sizing:border-box;margin:0;padding:0}
  html,body{width:1200px;height:800px;overflow:hidden;background:var(--white);font-family:"Raleway",sans-serif;color:var(--ink)}
  .page{position:relative;width:1200px;height:800px;overflow:hidden}

  /* header */
  .site-header{position:absolute;left:0;top:0;width:1200px;height:98px;background:var(--white);z-index:3}
  .brand{position:absolute;left:203px;top:30px;display:flex;align-items:center;gap:10px}
  .brand-name{color:var(--red);font-weight:600;font-size:21px;line-height:20px;letter-spacing:1.5px}
  .brand-mark{width:18px;height:18px;border-radius:50%;background:var(--ink)}
  .main-nav{position:absolute;top:42px;left:0;width:100%}
  .main-nav a{position:absolute;font-size:10px;font-weight:600;letter-spacing:.6px;color:var(--muted);text-decoration:none;text-transform:uppercase}
  .social{position:absolute;top:2px;left:900px;display:flex;gap:12px}
  .social span{width:22px;height:20px;background:#eef0f3;display:block}
  .appointments{position:absolute;top:82px;left:809px;width:182px;text-align:center;font-size:9px;font-weight:700;letter-spacing:.3px;color:var(--muted)}
  .phone-ribbon{position:absolute;top:101px;left:809px;width:182px;height:22px;z-index:4}
  .phone-ribbon span{position:absolute;inset:0;display:flex;align-items:center;justify-content:center;color:var(--white);font-size:9px;font-weight:700;letter-spacing:.4px}

  /* hero */
  .hero{position:absolute;left:0;top:98px;width:1200px;height:389px;background:var(--hero-dark);overflow:hidden}
  .hero-photo{position:absolute;left:520px;top:0;width:680px;height:389px;
    background:radial-gradient(ellipse at 62% 40%,#8c1a28 0%,#5e0b17 35%,transparent 70%),
               linear-gradient(90deg,var(--hero-dark) 0%,#3c0610 25%,#7d1220 60%,#9a1c2c 100%)}
  .hero-copy{position:absolute;left:0;top:96px;width:1194px;text-align:center;color:var(--white);z-index:2}
  .hero-kicker{font-size:30px;font-weight:400;line-height:32px;letter-spacing:.5px}
  .hero-title{font-size:31px;font-weight:600;line-height:34px;letter-spacing:.5px}
  .hero-tag{font-size:20px;font-weight:400;margin-top:10px}
  .hero-cta{display:inline-block;margin-top:13px;width:183px;height:33px;line-height:33px;background:rgba(40,8,16,.85);color:var(--red);font-size:14px;font-weight:600}

  .categories{position:absolute;left:203px;top:260px;display:flex;gap:17px;z-index:2}
  .category{width:184px;height:129px;background:var(--card-bg);text-align:center;padding-top:34px}
  .category h2{font-size:24px;font-weight:600;color:var(--white);line-height:28px}
  .category.is-muted h2{color:var(--card-title-muted)}
  .category a{display:block;margin:15px auto 0;width:134px;height:33px;line-height:33px;background:var(--red);color:var(--white);font-size:9px;font-weight:700;text-decoration:none}

  /* intro */
  .intro{position:absolute;left:0;top:487px;width:1200px;height:313px;background:var(--white)}
  .welcome{position:absolute;left:200px;top:40px;width:532px}
  .vision{position:absolute;left:787px;top:40px;width:210px;border-left:3px solid var(--rule);padding-left:17px;height:273px}
  .intro h3{font-size:19px;font-weight:600;letter-spacing:.3px;margin-bottom:16px}
  .intro p{font-size:11px;line-height:19px;color:var(--muted);margin-bottom:18px}
  .vision p{line-height:20.5px}
</style>
</head>
<body>
<div class="page">
  <header class="site-header">
    <div class="brand">
      <div class="brand-name">HARBOURLINE<br>COSMETIC</div>
      <span class="brand-mark"></span>
    </div>
    <div class="social" aria-label="Social links"><span></span><span></span><span></span></div>
    <nav class="main-nav">
      <a style="left:535px">About Us</a>
      <a style="left:620px">Procedures</a>
      <a style="left:721px">News</a>
      <a style="left:783px">Patient Resources</a>
      <a style="left:924px">Contact Us</a>
    </nav>
    <div class="appointments">CALL FOR APPOINTMENTS</div>
  </header>

  <div class="phone-ribbon">
    <svg width="182" height="22" viewBox="0 0 182 22"><polygon points="0,0 182,0 174,11 182,22 0,22 8,11" fill="var(--red-soft)"/></svg>
    <span>02 9000 4821</span>
  </div>

  <section class="hero">
    <div class="hero-photo" role="img" aria-label="Woman in a red silk drape stepping out from behind red theatre curtains"></div>
    <div class="hero-copy">
      <div class="hero-kicker">AT THE HARBOURLINE CENTRE OF</div>
      <h1 class="hero-title">COSMETIC PLASTIC SURGERY</h1>
      <p class="hero-tag">Your future looks beautiful.</p>
      <span class="hero-cta">LEARN MORE</span>
    </div>
    <div class="categories">
      <div class="category is-muted"><h2>BREAST</h2><a>LEARN MORE</a></div>
      <div class="category"><h2>BODY</h2><a>LEARN MORE</a></div>
      <div class="category is-muted"><h2>FACE</h2><a>LEARN MORE</a></div>
      <div class="category"><h2>NON SURGIAL</h2><a>LEARN MORE</a></div>
    </div>
  </section>

  <section class="intro">
    <div class="welcome">
      <h3>WELCOME TO HCS</h3>
      <p>You can expect beautiful results at the Harbourline Centre of Cosmetic Plastic Surgery. Offering unparalleled expertise in face, breast and body enhancement, including facelifts, breast augmentation / lift / reduction or tummy tucks. we offer total care at every step of your transformative journey.</p>
      <p>Dr Whitford is one of Australia's most eminent specialists in plastic and cosmetic surgery, and is supported by our highly qualified, professional team. As Sydney's premier plastic surgery clinic, we use the latest techniques to achieve natural results.</p>
    </div>
    <div class="vision">
      <h3>OUR VISION</h3>
      <p>With advanced techniques, expertise and constant client feedback, we aim to remain at the forefront of surgical rejuvenation and deliver outstanding results for every patient.</p>
    </div>
  </section>
</div>
</body>
</html>
```